ThisIsRayWendt.com needs a modern, eye-catching business card design

My name is Ray Wendt and I own a video training (software development industry) website. I need a business card design that is eye catching for when I travel to conferences or do seminars. I would prefer something simple but bold. Something along the lines of this: https://pixvaultcdn.example/design_img/512376/40918/40918_7720341_512376_image.jpg

Note that I do not have a specific logo, but I do have an caricature I use on my site of myself. I've not attached it because I'm not really a fan of having it on my business cards. I would prefer lettering instead of an image. You can go to my website (https://thisisraywendt.example) for inspiration.

I want to add the following information on my card (the order of these, their size, and their casing is up to you):

Ray Wendt
ray@ThisIsRayWendt.example
@ThisIsRayWendt
ThisIsRayWendt.com
vidstream.example/ThisIsRayWendt

I would also like to have somewhere on the card a small ad that says "Get a free course at https://ThisIsRayWendt.example/FreeCourse". Feel free to play with that wording or layout if you need. I would prefer this text to be at the bottom of the card and subtle. Some small eye-catching thing might be ok but nothing huge or garish.

I plan on printing this card at prixa.example (https://www.prixa.example/us/design-guidelines/business-cards.html). I would like it to be the standard size (3.66" x 2.16"). I would prefer rounded corners and horizontal orientation. This is a two-side design. I would prefer the side with all of the information be primarily white but I like color text (again, flexible on that). On the front side, I like simple. Maybe just ThisIsRayWendt.com (casing on that is up to you - whatever looks and reads the best - that goes for all of the casing). As for font choices, I prefer a modern, clean font. For example, Open Sans Light can be a nice option.

Website Info (might be helpful for the card):
Color Palette

Darkest blue - #263246
Alternate blue - #2F4E6A
Light blue - #2A98C3
Orange - #FF6201
White - #FFFFFF

Font for Ray Wendt Logo

Jellyka Estryas Handwriting
http://www.typeharborfree.example/jellyka_estryas_handwriting.font

Fonts for Site Content and VidStream Thumbnails

Lovelo (bold title font)
http://www.glyphmill.example/lovelo-font/

Open Sans (body font)
http://www.letterburrow.example/fonts/open-sans

Industry/Entity Type

Software Development

Contact Information for Business Card

Ray Wendt
ray@ThisIsRayWendt.example
@ThisIsRayWendt
ThisIsRayWendt.com
vidstream.example/ThisIsRayWendt

Get a free course at https://ThisIsRayWendt.example/FreeCourse

Colors

Designer to choose colors to be used in the design.

Requirements
Nice to have
• Modern color - maybe primarily a color on the front and then that color as an accent on the back.
Should not have
• Lots of colors - I LOVE color but do not want a rainbow of colors on the card.

```html
<!DOCTYPE html>
<html lang="en">
<head>
<meta charset="utf-8">
<title>Ray Wendt – Business Card</title>
<link rel="stylesheet" href="https://fonts.googleapis.com/css2?family=Montserrat:wght@400&family=Open+Sans:wght@400&display=swap">
<style>
  :root {
    --sheet-grey: #c9c9c9;
    --card-white: #ffffff;
    --navy: #212556;
    --deep-blue: #1f3f72;
    --mid-blue: #1a6aa6;
    --light-blue: #1ba1e2;
    --contact-blue: #4a8fc4;
    --accent-orange: #d9531e;
  }
  * { margin: 0; padding: 0; box-sizing: border-box; }
  html, body {
    width: 1012px; height: 1200px; overflow: hidden;
    background: var(--sheet-grey);
  }
  .sheet { position: relative; width: 1012px; height: 1200px; }
  .card {
    position: absolute; left: 10px; width: 992px; height: 585px;
    background: var(--card-white);
    border-radius: 68px; overflow: hidden;
  }
  .card--front { top: 7px; }
  .card--back { top: 601px; }
  .card__panel {
    position: absolute; left: 0; top: 0; width: 265px; height: 585px;
    background: linear-gradient(90deg, var(--navy) 0%, var(--navy) 70%, var(--mid-blue) 88%, var(--light-blue) 100%);
  }
  .wordmark {
    position: absolute;
    font-family: "Montserrat", sans-serif; font-weight: 400;
    color: var(--navy); white-space: nowrap;
  }
  .card--front .wordmark {
    left: 572px; top: 255px; transform: translate(-50%, -50%);
    font-size: 68px;
  }
  .card--back .wordmark--main {
    right: 73px; top: 135px; transform: translateY(-50%);
    font-size: 66px;
  }
  .card--back .wordmark--small {
    left: 52px; top: 487px; transform: translateY(-50%);
    font-size: 30px; color: var(--card-white);
  }
  .contact-list { list-style: none; }
  .contact {
    position: absolute; right: 99px;
    display: flex; align-items: center; gap: 10px;
    transform: translateY(-50%);
    font-family: "Montserrat", sans-serif; font-size: 23px;
    color: var(--contact-blue); white-space: nowrap;
  }
  .contact__badge {
    width: 40px; height: 40px; border-radius: 50%;
    display: flex; align-items: center; justify-content: center;
    flex: none;
  }
  .contact--email { top: 273px; }
  .contact--email .contact__badge { background: var(--navy); }
  .contact--social { top: 330px; }
  .contact--social .contact__badge { background: var(--deep-blue); }
  .contact--web { top: 387px; }
  .contact--web .contact__badge { background: var(--mid-blue); }
  .contact--video { top: 444px; }
  .contact--video .contact__badge { background: var(--light-blue); }
  .promo {
    position: absolute; right: 99px; top: 525px; transform: translateY(-50%);
    font-family: "Open Sans", sans-serif; font-size: 17px;
    color: var(--accent-orange); white-space: nowrap;
  }
</style>
</head>
<body>
<main class="sheet">

  <section class="card card--front" aria-label="Card front">
    <div class="card__panel" role="img" aria-label="Decorative navy and blue wave artwork"></div>
    <p class="wordmark">Ray Wendt</p>
  </section>

  <section class="card card--back" aria-label="Card back">
    <div class="card__panel" role="img" aria-label="Decorative navy and blue wave artwork"></div>

    <p class="wordmark wordmark--main">Ray Wendt</p>
    <p class="wordmark wordmark--small">Ray Wendt</p>

    <ul class="contact-list">
      <li class="contact contact--email">
        <span>ray@ThisIsRayWendt.example</span>
        <span class="contact__badge">
          <svg width="22" height="16" viewBox="0 0 22 16" aria-hidden="true">
            <rect x="1" y="1" width="20" height="14" fill="none" stroke="#fff" stroke-width="2"/>
            <path d="M1 1 L11 9 L21 1 M1 15 L8 7 M21 15 L14 7" fill="none" stroke="#fff" stroke-width="1.6"/>
          </svg>
        </span>
      </li>
      <li class="contact contact--social">
        <span>@ThisIsRayWendt</span>
        <span class="contact__badge"></span>
      </li>
      <li class="contact contact--web">
        <span>ThisIsRayWendt.com</span>
        <span class="contact__badge">
          <svg width="24" height="24" viewBox="0 0 24 24" aria-hidden="true">
            <g fill="none" stroke="#fff" stroke-width="1.6">
              <circle cx="12" cy="12" r="10"/>
              <ellipse cx="12" cy="12" rx="4.5" ry="10"/>
              <path d="M2 12 H22 M4 6.5 H20 M4 17.5 H20"/>
            </g>
          </svg>
        </span>
      </li>
      <li class="contact contact--video">
        <span>vidstream.example/ThisIsRayWendt</span>
        <span class="contact__badge"></span>
      </li>
    </ul>

    <p class="promo">Get a free course at https://ThisIsRayWendt.example/FreeCourse</p>
  </section>

</main>
</body>
</html>
```